Business Card - Professional Minimalist - Double sided

We appreciate minimalist logo/web/collateral designs that allow design to tell a story. We want to relay a professional image/approach but throwing in a splash of modern when we’re able so long as it’s not distracting. Think 75% classic corporate, 25% modern. Open to black or white design, not sure which might look the best.

Target Market(s)

Senior executives or related government affairs contacts within the agriculture, energy, and defense industries (i.e., potential clients) but located outside of Washington, DC. Most potential clients based in DC with be familiar with both of us and our shared history.

Industry/Entity Type

Consulting

Contact Information for Business Card

Name: Daniel R. Whitlock
Title: Co-Founder & Partner
Address: 418 Bramblewood Ave. SE | Suite 2716 | Washington, D.C. 20019
Phone: (202) 555-0187
Email: Daniel@HollerbyWhitlock.com

Font styles to use
Serif

Colors

Designer to choose only greyscale colors for use in the design.

Requirements
Must have
• Name: Daniel R. Whitlock
Phone: (202) 555-0187

```html
<!DOCTYPE html>
<html lang="en">
<head>
<meta charset="utf-8">
<title>Hollerby Whitlock Group – Business Card</title>
<link href="https://fonts.googleapis.com/css2?family=Marcellus&family=Roboto:wght@400;700&display=swap" rel="stylesheet">
<style>
  :root {
    --page-bg: #2b2b2b;
    --card-bg: #1c1c1c;
    --ink-strong: #8a8a8a;
    --ink: #bdbdbd;
    --ink-soft: #6f6f6f;
    --rule: #5a5a5a;
    --emboss: #262626;
  }
  * { margin: 0; padding: 0; box-sizing: border-box; }
  html, body { width: 1200px; height: 900px; overflow: hidden; }
  body {
    background: var(--page-bg);
    display: flex;
    flex-direction: column;
    align-items: center;
    justify-content: center;
    gap: 24px;
  }
  .card {
    width: 700px;
    height: 400px;
    background: var(--card-bg);
    box-shadow: 0 10px 30px rgba(0,0,0,0.45);
    position: relative;
  }

  /* Front */
  .card--front { display: flex; align-items: center; padding: 0 48px; }
  .brand { width: 300px; }
  .brand__row { display: flex; align-items: center; gap: 12px; }
  .brand__mark {
    width: 30px; height: 30px;
    background: var(--ink-soft);
    flex: none;
  }
  .brand__name {
    font-family: "Marcellus", serif;
    font-size: 23px;
    letter-spacing: 1px;
    color: var(--ink-soft);
    text-transform: uppercase;
    white-space: nowrap;
  }
  .brand__rule { height: 1px; background: var(--rule); margin: 8px 0 4px 42px; }
  .brand__group {
    font-family: "Marcellus", serif;
    font-size: 11px;
    letter-spacing: 6px;
    color: var(--ink-soft);
    text-align: right;
  }
  .divider { width: 1px; height: 150px; background: var(--rule); margin: 0 22px 0 26px; flex: none; }
  .contact { font-family: "Roboto", sans-serif; color: var(--ink); font-size: 14.5px; line-height: 1.45; }
  .contact__name { font-weight: 700; font-size: 19px; color: var(--ink-strong); line-height: 1.3; }
  .contact__lines { margin-bottom: 4px; }
  .contact__item { display: flex; align-items: center; gap: 7px; }
  .contact__item svg { width: 11px; height: 11px; fill: var(--ink-soft); flex: none; }

  /* Back */
  .card--back { display: flex; align-items: center; justify-content: center; gap: 16px; }
  .back__mark { width: 56px; height: 56px; background: var(--emboss); box-shadow: inset 1px 1px 2px rgba(0,0,0,0.6), 1px 1px 0 rgba(255,255,255,0.04); }
  .back__name {
    font-family: "Marcellus", serif;
    font-size: 34px;
    letter-spacing: 2px;
    text-transform: uppercase;
    color: var(--emboss);
    text-shadow: 1px 1px 0 rgba(255,255,255,0.05);
  }
</style>
</head>
<body>
  <section class="card card--front">
    <div class="brand">
      <div class="brand__row">
        <span class="brand__mark"></span>
        <span class="brand__name">Hollerby Whitlock</span>
      </div>
      <div class="brand__rule"></div>
      <div class="brand__group">GROUP</div>
    </div>
    <div class="divider"></div>
    <div class="contact">
      <div class="contact__name">Daniel R. Whitlock</div>
      <div class="contact__lines">
        Co-Founder &amp; Partner<br>
        418 Bramblewood Ave. SE<br>
        Suite 2716 | Washington, D.C. 20019
      </div>
      <div class="contact__item">
        <svg viewBox="0 0 24 24"><path d="M6.6 10.8a15.1 15.1 0 0 0 6.6 6.6l2.2-2.2c.3-.3.7-.4 1-.2 1.1.4 2.3.6 3.6.6.6 0 1 .4 1 1V20c0 .6-.4 1-1 1A17 17 0 0 1 3 4c0-.6.4-1 1-1h3.5c.6 0 1 .4 1 1 0 1.3.2 2.5.6 3.6.1.3 0 .7-.2 1z"/></svg>
        (202) 555-0187
      </div>
      <div class="contact__item">
        <svg viewBox="0 0 24 24"><path d="M2 5h20v14H2z M2 5l10 8 10-8" fill="none" stroke="#6f6f6f" stroke-width="2"/></svg>
        Daniel@HollerbyWhitlock.com
      </div>
      <div class="contact__item">
        <svg viewBox="0 0 24 24"><circle cx="12" cy="12" r="10" fill="none" stroke="#6f6f6f" stroke-width="2"/><path d="M2 12h20M12 2c3 3 3 17 0 20M12 2c-3 3-3 17 0 20" fill="none" stroke="#6f6f6f" stroke-width="1.6"/></svg>
        HollerbyWhitlock.com
      </div>
    </div>
  </section>

  <section class="card card--back">
    <span class="back__mark"></span>
    <span class="back__name">Hollerby Whitlock</span>
  </section>
</body>
</html>
```